Tress Radiant from root to soul. Hair stylist that specializes in extensions.

I am Marisol I am a hair stylist and I would like a website designed for my hair business.

I currently book clients via my profile on glamslot.net/marisolbreck

I need a professional website ( tressradiantfromroottosoul.net ) to display photos and prices for services offered.

I would like to have a home page with a brief bio, Image with logo and testimonials at the bottom, and a header with tab that include: menu of services, gallery,and FAQs.

On the "Services" page, I'm not interested in photos on this page. Just the name of the service, brief description, and pricing. I would also like to have, on this page, "Appointment Request" with fields that include: Name, service requested, desired time frame (morning, afternoon, evening), and contact number and email

On the "Gallery" page, I would like pictures only, but arranged and/or presented in a creative way...

Target Market(s)

Women ages 25-55 who interested in hair extension services.

Industry/Entity Type

Hair And Beauty

Coding

Coded - Design and coding required

Number of Pages Required

5+ page

Font styles to use
Sans Serif

Requirements
Must have
• Must include tabs that include, Menu of services offered, a quik pae link to pay deposits with ease, location, contact information, photo gallery, and policy/faqs.
Nice to have
• If possible i would like to stream music with the ability to be silenced. I would like a neutral color palette tans and beige.
Should not have
• stock images

```html
<!DOCTYPE html>
<html lang="en">
<head>
<meta charset="utf-8">
<title>Tress Radiant from root to soul</title>
<link href="https://fonts.googleapis.com/css2?family=Raleway:wght@400;500;600;700;800&family=Dancing+Script:wght@600;700&display=swap" rel="stylesheet">
<style>
:root{
  --yellow:#e3c500;
  --ink:#222222;
  --text:#444444;
  --hero:#1d1c1c;
  --slate:#a9b8b6;
  --footer:#3a3a3e;
  --footer-deep:#232325;
  --footer-text:#c9c9cc;
  --white:#ffffff;
}
*{margin:0;padding:0;box-sizing:border-box}
html,body{width:1200px;height:2579px;overflow:hidden}
body{position:relative;background:var(--white);font-family:"Raleway",sans-serif;color:var(--text)}
.abs{position:absolute}
.script{font-family:"Dancing Script",cursive}

/* header */
.site-header{left:0;top:0;width:1200px;height:132px;background:var(--white)}
.brand{left:107px;top:28px;color:var(--ink);font-weight:800;line-height:1}
.brand .name{font-size:40px;letter-spacing:1px}
.brand .tag{font-size:13px;letter-spacing:3.2px;margin-top:8px}
.book-btn{left:701px;top:21px;width:214px;height:44px;background:var(--yellow);color:var(--white);font-size:17px;font-weight:500;display:flex;align-items:center;justify-content:center}
.phone{left:937px;top:27px;display:flex;align-items:center;gap:8px;font-size:19px;font-weight:600;color:var(--ink)}
.phone .dot{width:24px;height:24px;border-radius:50%;background:var(--ink);display:flex;align-items:center;justify-content:center}
.main-nav{left:490px;top:83px;height:37px;display:flex;align-items:center;font-size:15px;font-weight:600;color:var(--ink);letter-spacing:.3px}
.main-nav span{margin-right:26px}
.main-nav .active{background:var(--ink);color:var(--yellow);height:37px;width:86px;display:flex;align-items:center;justify-content:center;margin-right:26px}

/* hero */
.hero{left:0;top:132px;width:1200px;height:506px;background:var(--hero);overflow:hidden}
.hero-photo{left:520px;top:0;width:680px;height:506px;background:radial-gradient(ellipse at 55% 45%,#a7725c 0%,#6b4232 35%,#2e211c 70%,var(--hero) 100%)}
.hero-title{left:103px;top:115px;color:var(--white);font-size:53px;font-weight:400;line-height:69px;letter-spacing:1px}
.hero-script{left:101px;top:255px;color:var(--white);font-size:68px;font-weight:700;font-style:italic}
.hero-btn{left:100px;top:368px;width:213px;height:52px;background:var(--yellow);color:var(--ink);font-size:26px;font-weight:600;display:flex;align-items:center;justify-content:center}
.slide-arrow{top:232px;width:76px;height:45px;background:#6a6a6a;display:flex;align-items:center;justify-content:center}
.slide-arrow.left{left:0}
.slide-arrow.right{left:1124px}

/* section heading */
.section-title{display:flex;align-items:center;gap:14px;font-size:38px;color:var(--ink)}
.section-title::before{content:"";width:4px;height:36px;background:var(--yellow)}

/* about */
.about-title{left:100px;top:676px}
.about-copy{left:100px;top:734px;width:706px;font-size:12.7px;line-height:22.5px;color:#555}
.about-copy p{margin-bottom:9px}
.read-more{left:100px;top:897px;width:108px;height:33px;background:var(--ink);color:var(--white);font-size:12.5px;font-weight:700;display:flex;align-items:center;justify-content:center}
.about-photo{left:827px;top:696px;width:273px;height:234px;border:2px solid #e2e2e2;background:linear-gradient(135deg,#cfd6dc 0%,#3a5fa8 45%,#d8c2b2 75%,#f3eee9 100%)}

/* services */
.services{left:0;top:976px;width:1200px;height:516px;background:linear-gradient(90deg,#c4cfcd 0%,var(--slate) 45%,var(--slate) 100%)}
.services-title{left:100px;top:1008px;color:var(--white)}
.service-card{top:1088px;width:232px;height:270px;border:3px solid #111;background:linear-gradient(160deg,#f2f2f2 0%,#9a9a9a 55%,#3c3c3c 100%);overflow:hidden}
.service-card .label{position:absolute;left:0;bottom:0;width:100%;height:51px;background:rgba(20,20,20,.78);color:var(--white);font-size:16px;font-weight:700;line-height:20px;text-align:center;display:flex;align-items:center;justify-content:center}
.carousel-btn{top:1406px;width:53px;height:33px;display:flex;align-items:center;justify-content:center}
.carousel-btn.prev{left:547px;background:#3a3a3a}
.carousel-btn.next{left:600px;background:var(--white)}

/* gallery */
.gallery-title{left:100px;top:1533px}
.tile{overflow:hidden}
.overlay{position:absolute;inset:0;background:rgba(222,200,20,.82);display:flex;flex-direction:column;align-items:center;justify-content:center;gap:18px;color:var(--white)}
.overlay .cap{font-size:28px;font-weight:600}
.overlay .icons{display:flex;gap:22px}

/* footer */
.site-footer{left:0;top:2214px;width:1200px;height:321px;background:var(--footer);color:var(--footer-text)}
.foot-head{top:2250px;color:var(--white);font-size:14px;font-weight:700;letter-spacing:.3px}
.foot-links{left:103px;top:2283px;list-style:none;font-size:12.5px}
.foot-links li{height:33.6px;display:flex;align-items:center;gap:12px}
.foot-links li::before{content:"";width:4px;height:4px;border-radius:50%;background:var(--footer-text)}
.divider{top:2250px;width:1px;height:260px;background:#4b4b50}
.contact-row{left:280px;display:flex;gap:16px;font-size:12.3px;line-height:18px}
.contact-row svg{flex:none;margin-top:2px}
.field{left:540px;width:266px;border:1px solid #c9c9cc;border-radius:3px;font-size:12px;color:var(--footer-text);padding:9px 12px}
.submit{left:540px;top:2453px;width:103px;height:33px;background:var(--white);color:var(--ink);font-weight:700;font-size:14px;border-radius:3px;display:flex;align-items:center;justify-content:center}
.feed{width:108px;height:108px;border:2px solid var(--white)}
.copyright{left:0;top:2535px;width:1200px;height:44px;background:var(--footer-deep);color:var(--footer-text);font-size:12px;display:flex;align-items:center;justify-content:center}
</style>
</head>
<body>

<header class="site-header abs">
  <div class="brand abs">
    <div class="name">TRESS RADIANT</div>
    <div class="tag">FROM ROOT TO SOUL</div>
  </div>
  <div class="book-btn abs">Book An Appointment</div>
  <div class="phone abs">
    <span class="dot"><svg width="12" height="14" viewBox="0 0 12 14"><rect x="2" y="1" width="8" height="12" rx="1.5" fill="none" stroke="#fff" stroke-width="1.6"/><line x1="4" y1="4" x2="8" y2="4" stroke="#fff" stroke-width="1.4"/></svg></span>
    (555)0142-387
  </div>
  <nav class="main-nav abs">
    <span class="active">HOME</span><span>BIO</span><span>SERVICES</span><span>GALLERY</span><span>PRICE</span><span>FAQ's</span><span>CONTACT US</span>
  </nav>
</header>

<section class="hero abs">
  <div class="hero-photo abs" role="img" aria-label="Portrait of a woman with long brown hair lifting her sunglasses"></div>
  <h1 class="hero-title abs">GET THE LONG HAIR<br>YOU'VE NEVER</h1>
  <div class="hero-script script abs">HAD BEFORE!</div>
  <div class="hero-btn abs">Contact Now</div>
  <div class="slide-arrow left abs"><svg width="14" height="20" viewBox="0 0 14 20"><path d="M11 2 L3 10 L11 18" fill="none" stroke="#fff" stroke-width="3"/></svg></div>
  <div class="slide-arrow right abs"><svg width="14" height="20" viewBox="0 0 14 20"><path d="M3 2 L11 10 L3 18" fill="none" stroke="#fff" stroke-width="3"/></svg></div>
</section>

<h2 class="section-title script about-title abs">About Me</h2>
<div class="about-copy abs">
  <p>Lorem ipsum dolor sit amet, consectetur adipiscing elit. Aenean venenatis congue tempus. Sed aliquet magna non justo finibus, ac tincidunt nibh viverra. Nam quam libero, aliquet nec nibh eget, rutrum porta ligula. Vestibulum lacinia semper turpis tempor luctus. Cras lacinia diam eu justo viverra, non cursus odio tincidunt. Morbi euismod neque vel leo finibus, non mattis lorem eleifend. Suspendisse potenti.</p>
  <p>Nunc pretium finibus purus et porta. Nulla pulvinar et urna eu mattis. Suspendisse sit amet est posuere, ultrices elit sed, ornare est. Morbi sollicitudin lobortis eros. Sed lacinia eget leo quis dapibus.</p>
</div>
<div class="read-more abs">Read More</div>
<div class="about-photo abs" role="img" aria-label="Stylist finishing a client's hair with spray"></div>

<section class="services abs" role="img" aria-label="Soft faded portrait behind the services list"></section>
<h2 class="section-title script services-title abs">Our Services</h2>
<div class="service-card abs" style="left:100px" role="img" aria-label="Woman with long straight hair"><div class="label">CLIP IN HAIR<br>EXTENSIONS</div></div>
<div class="service-card abs" style="left:356px" role="img" aria-label="Woman with long wavy hair"><div class="label">NAIL/U TIP HAIR<br>EXTENSIONS</div></div>
<div class="service-card abs" style="left:612px" role="img" aria-label="Woman with flowing hair"><div class="label">MICRO LOOP/LINK HAIR<br>EXTENSIONS</div></div>
<div class="service-card abs" style="left:868px" role="img" aria-label="Woman with styled updo"><div class="label">STICK/I TIP HAIR<br>EXTENSIONS</div></div>
<div class="carousel-btn prev abs"><svg width="18" height="14" viewBox="0 0 18 14"><path d="M8 1 L2 7 L8 13 V9 H16 V5 H8 Z" fill="none" stroke="#fff" stroke-width="1.4"/></svg></div>
<div class="carousel-btn next abs"><svg width="18" height="14" viewBox="0 0 18 14"><path d="M10 1 L16 7 L10 13 V9 H2 V5 H10 Z" fill="none" stroke="#333" stroke-width="1.4"/></svg></div>

<h2 class="section-title script gallery-title abs">Photo Gallery</h2>
<div class="tile abs" style="left:100px;top:1597px;width:270px;height:273px;background:linear-gradient(150deg,#f3d9a8,#d69a5c 60%,#a9693e)" role="img" aria-label="Woman in round sunglasses"></div>
<div class="tile abs" style="left:370px;top:1597px;width:278px;height:273px;background:linear-gradient(150deg,#f0e07a,#c9a93c)" role="img" aria-label="Woman with sunglasses under a highlight overlay">
  <div class="overlay">
    <div class="cap">Lorem Ispum</div>
    <div class="icons">
      <svg width="18" height="18" viewBox="0 0 18 18"><circle cx="7.5" cy="7.5" r="5.5" fill="none" stroke="#fff" stroke-width="2"/><line x1="11.5" y1="11.5" x2="16.5" y2="16.5" stroke="#fff" stroke-width="2.4"/></svg>
      <svg width="18" height="18" viewBox="0 0 18 18"><rect x="2" y="5" width="11" height="11" fill="none" stroke="#fff" stroke-width="1.8"/><path d="M8 10 L16 2 M11 2 H16 V7" fill="none" stroke="#fff" stroke-width="1.8"/></svg>
      <svg width="18" height="18" viewBox="0 0 18 18"><path d="M9 15 L2.5 8.5 A3.6 3.6 0 0 1 9 4.2 A3.6 3.6 0 0 1 15.5 8.5 Z" fill="none" stroke="#fff" stroke-width="1.8"/></svg>
    </div>
  </div>
</div>
<div class="tile abs" style="left:648px;top:1597px;width:177px;height:273px;background:linear-gradient(160deg,#f1e7d8,#c7a587 60%,#8f6b52)" role="img" aria-label="Woman with blonde hair"></div>
<div class="tile abs" style="left:825px;top:1597px;width:275px;height:273px;background:linear-gradient(150deg,#f6ead4,#c99862 55%,#7a5130)" role="img" aria-label="Woman with curly brown hair"></div>
<div class="tile abs" style="left:100px;top:1870px;width:484px;height:301px;background:linear-gradient(120deg,#f5e9cf,#d5a26d 50%,#8a5a39)" role="img" aria-label="Woman wearing a headband"></div>
<div class="tile abs" style="left:584px;top:1870px;width:516px;height:301px;background:linear-gradient(110deg,#c99a67,#efd9b0 55%,#fbf4e2)" role="img" aria-label="Woman with long curly hair"></div>

<footer class="site-footer abs">
</footer>
<div class="foot-head abs" style="left:101px">QUICK LINKS</div>
<ul class="foot-links abs">
  <li>Home</li><li>Bio</li><li>Services</li><li>Gallery</li><li>Price</li><li>Faq's</li><li>Contact Us</li>
</ul>
<div class="divider abs" style="left:246px"></div>
<div class="foot-head abs" style="left:280px">CONTACT INFORMATION</div>
<div class="contact-row abs" style="top:2290px">
  <svg width="12" height="16" viewBox="0 0 12 16"><path d="M6 15 C6 15 1 9 1 5.5 A5 5 0 0 1 11 5.5 C11 9 6 15 6 15 Z" fill="#c9c9cc"/><circle cx="6" cy="5.5" r="1.8" fill="#3a3a3e"/></svg>
  <span>16 Lorem ipsum dolor sit<br>sed benetion.<br>Street no-123456</span>
</div>
<div class="contact-row abs" style="top:2362px">
  <svg width="13" height="13" viewBox="0 0 13 13"><path d="M2 1 L5 1 L6 4 L4.5 5.5 A7 7 0 0 0 7.5 8.5 L9 7 L12 8 L12 11 C6 12 1 7 2 1 Z" fill="#c9c9cc"/></svg>
  <span style="color:#fff;font-weight:600">(555) 318-2046</span>
</div>
<div class="contact-row abs" style="top:2395px">
  <svg width="14" height="13" viewBox="0 0 14 13"><rect x="3" y="0.5" width="8" height="4" fill="#c9c9cc"/><rect x="0.5" y="4.5" width="13" height="6" rx="1" fill="#c9c9cc"/><rect x="3" y="8" width="8" height="4.5" fill="#3a3a3e" stroke="#c9c9cc"/></svg>
  <span>555.318.2047</span>
</div>
<div class="contact-row abs" style="top:2428px">
  <svg width="14" height="11" viewBox="0 0 14 11"><rect x="0.5" y="0.5" width="13" height="10" fill="#c9c9cc"/><path d="M0.5 0.5 L7 6 L13.5 0.5" fill="none" stroke="#3a3a3e" stroke-width="1.2"/></svg>
  <span>hello@tressradiant.net</span>
</div>
<div class="divider abs" style="left:507px"></div>
<div class="foot-head abs" style="left:540px">QUICK INQUIRY</div>
<div class="field abs" style="top:2288px;height:35px">Name</div>
<div class="field abs" style="top:2329px;height:35px">Phone</div>
<div class="field abs" style="top:2372px;height:66px">Message</div>
<div class="submit abs">SUBMIT</div>
<div class="divider abs" style="left:837px"></div>
<div class="foot-head abs" style="left:873px">PHOTO FEED</div>
<div class="feed abs" style="left:873px;top:2283px;background:linear-gradient(150deg,#e8d2b8,#9c6d52)" role="img" aria-label="Feed photo of a woman with long hair"></div>
<div class="feed abs" style="left:994px;top:2283px;background:linear-gradient(150deg,#f0ece6,#a58870)" role="img" aria-label="Feed photo of a woman in sunglasses"></div>
<div class="feed abs" style="left:873px;top:2402px;background:linear-gradient(150deg,#c28a68,#5a3424)" role="img" aria-label="Feed photo of a woman with auburn hair"></div>
<div class="feed abs" style="left:994px;top:2402px;background:linear-gradient(150deg,#f5e6c8,#c9a36c)" role="img" aria-label="Feed photo of a blonde woman in sunglasses"></div>

<div class="copyright abs">Copyright © 2016 Tress Radiant from root to soul. All Rights Reserved.</div>

</body>
</html>
```